Harbor Mortgage Relief

Please help us give our website a remake or a FACELIFT. It is not very good but it says what we need it to say. But the design is terrible.
I would like our new design font and logo to be used as the theme.

I also want more photos on the site.

I also want consistency with the pages so they look clean.

We want the professionals to do this, let's see what you got!

Thank you!
Updates

Project Deadline Extended
Reason: I can understand you want to be paid. So I will commit to the fee but I want you to have time to make a KICK ASS website for me dudes! Thanks

HI!  Just wanted to say thanks for your time on these.  A lot are great.  However the firefighters have nothing to do with Foreclosure.  We are saving peoples homes from the bank taking them and selling them.   I LOVE the house photos and the families on the website.  That is the direction we like.  THanks.

THANK U ALL FOR THE WORK!   I like a few ending in the numbers: 147  733  693  536  620  478  727  508     I will go over them and choose one soon.  Thank you.   You will be paid shortly. 

Requirements
Must have
• Bright, Upbeat photos. Color scheme should be in order. We like icons on the bottom. not just text.

```html
<!DOCTYPE html>
<html lang="en">
<head>
<meta charset="utf-8">
<title>Harbor Mortgage Relief – Financing Options</title>
<link rel="stylesheet" href="https://fonts.googleapis.com/css2?family=Arimo:wght@400;700&family=Tinos:wght@400;700&display=swap">
<style>
:root{
  --red:#e1262d;
  --blue:#1a9be0;
  --phone-blue:#1b8fd6;
  --text:#555;
  --page-bg:#ececed;
  --white:#fff;
  --nav-top:#6a6a6a;
  --nav-bottom:#3a3a3a;
  --nav-active:#2b2b2b;
  --footer-top:#0f4f8a;
  --footer-bottom:#062a52;
  --footer-text:#e8eef6;
  --footer-head:#4fb3ef;
}
*{box-sizing:border-box;margin:0;padding:0}
html,body{width:815px;height:1200px;overflow:hidden}
body{position:relative;background:var(--page-bg);font-family:"Arimo",Arial,sans-serif;color:var(--text)}
a{color:inherit;text-decoration:none}
ul{list-style:none}

.site-header{position:absolute;left:0;top:0;width:815px;height:146px;background:var(--white)}
.utility-tab{position:absolute;left:621px;top:0;width:88px;height:19px;background:#e4e4e4;font-size:8px;color:#777;text-align:center;line-height:20px}
.brand{position:absolute;left:116px;top:42px;display:flex;align-items:center;gap:10px}
.brand-mark{width:46px;height:46px;border-radius:50%;background:var(--red)}
.brand-name{font-weight:700;font-size:17px;line-height:17px;color:var(--red);text-transform:uppercase;width:160px}
.call-line{position:absolute;right:106px;top:58px;display:flex;align-items:baseline;gap:8px}
.call-label{font-size:12px;color:#555}
.call-number{font-family:"Tinos",serif;font-size:27px;color:var(--phone-blue)}

.main-nav{position:absolute;left:105px;top:105px;width:604px;height:31px;background:linear-gradient(var(--nav-top),var(--nav-bottom));display:flex;align-items:stretch}
.main-nav a{display:flex;align-items:center;justify-content:center;color:#f2f2f2;font-size:11px;border-right:1px solid #2f2f2f;border-left:1px solid #777}
.nav-home{width:74px}
.nav-about{width:80px}
.nav-services{width:84px}
.nav-financing{width:138px;background:var(--nav-active)}
.nav-contact{width:94px}
.nav-search{position:absolute;right:9px;top:6px;width:121px;height:19px;background:var(--white);display:flex;align-items:center;padding-left:6px;font-size:8px;color:#999}
.nav-search-btn{position:absolute;right:0;top:0;width:18px;height:19px;background:var(--red);display:flex;align-items:center;justify-content:center}

.page-title{position:absolute;left:105px;top:190px;font-family:"Tinos",serif;font-variant:small-caps;font-size:19px;color:var(--red);letter-spacing:.5px}
.title-rule{position:absolute;left:105px;top:213px;width:602px;height:1px;background:#cfcfcf}

.article{position:absolute;left:105px;top:236px;width:417px;font-size:12.3px;line-height:20.7px;text-align:justify}
.article p{margin-bottom:20.7px}

.side-links{position:absolute;left:562px;top:236px;font-size:9.4px;color:var(--blue)}
.side-links li{position:relative;padding-left:15px;line-height:20.3px;width:150px}
.side-links li::before{content:"»";position:absolute;left:0;color:var(--red)}
.side-links .gap{height:20px}
.side-photo{position:absolute;left:578px;width:117px;height:75px;border:2px solid var(--white)}
.photo-couple{top:515px;background:linear-gradient(135deg,#e9dcc0,#7c8a5a)}
.photo-contract{top:606px;background:linear-gradient(135deg,#f2f4f7,#3a5fa8)}
.photo-family{top:698px;background:linear-gradient(160deg,#b9c8a8,#3f7a2c)}

.section-rule{position:absolute;left:105px;top:803px;width:592px;height:1px;background:#cfcfcf}

.testimonial{position:absolute;left:106px;top:817px;width:593px;height:112px;background:var(--white);border:1px solid #dcdcdc;border-radius:4px}
.testimonial-photo{position:absolute;left:11px;top:10px;width:138px;height:91px;background:linear-gradient(135deg,#c9b9a0,#b3262a 60%,#2b2b2b)}
.testimonial-title{position:absolute;left:292px;top:10px;font-family:"Tinos",serif;font-variant:small-caps;font-size:22px;color:var(--red);letter-spacing:.5px}
.quote-mark{position:absolute;font-family:"Tinos",serif;font-size:38px;color:#888;font-weight:700}
.quote-open{left:170px;top:26px}
.quote-close{left:535px;top:58px}
.testimonial-text{position:absolute;left:202px;top:40px;width:360px;font-family:"Tinos",serif;font-size:12px;line-height:19px;color:#666;letter-spacing:.3px}
.testimonial-author{position:absolute;left:200px;top:84px;font-size:10px;color:var(--blue)}

.site-footer{position:absolute;left:0;top:985px;width:815px;height:215px;background:radial-gradient(ellipse at 50% 0%,var(--footer-top),var(--footer-bottom) 80%);color:var(--footer-text)}
.footer-col{position:absolute;top:50px}
.footer-col h3{font-size:13px;color:var(--footer-head);font-weight:700;margin-bottom:4px}
.footer-col li{font-size:7.6px;line-height:13px}
.col-about{left:119px}
.col-advice{left:218px}
.col-join{left:303px}
.newsletter{position:absolute;left:379px;top:50px}
.newsletter h3{font-size:13px;color:var(--white);font-weight:700;margin-bottom:7px}
.newsletter-input{position:absolute;left:-3px;top:20px;width:151px;height:23px;background:var(--white);border-radius:3px;font-size:8.5px;color:#777;padding:7px 9px}
.newsletter-btn{position:absolute;left:156px;top:20px;width:75px;height:23px;background:var(--red);border-radius:3px;color:var(--white);font-size:10.5px;font-weight:700;text-align:center;line-height:23px}
.social{position:absolute;left:641px;top:70px;display:flex;gap:3px}
.social span{width:20px;height:20px;background:#e8e8e8;border-radius:2px}
.footer-rule{position:absolute;left:0;top:142px;width:815px;height:1px;background:rgba(255,255,255,.1)}
.legal{position:absolute;left:119px;top:164px;font-size:7.6px}
.copyright{position:absolute;left:119px;top:178px;font-size:7.6px;color:var(--footer-head)}
</style>
</head>
<body>

<header class="site-header">
  <div class="utility-tab">Login &nbsp;|&nbsp; Contacts</div>
  <a class="brand" href="#">
    <span class="brand-mark"></span>
    <span class="brand-name">Harbor Mortgage Relief</span>
  </a>
  <div class="call-line">
    <span class="call-label">Call Toll-Free Now</span>
    <span class="call-number">877-555-0142</span>
  </div>
  <nav class="main-nav">
    <a class="nav-home" href="#" aria-label="Home">
      <svg width="16" height="14" viewBox="0 0 16 14"><path d="M8 0 0 7h2v7h4V9h4v5h4V7h2z" fill="#fff"/></svg>
    </a>
    <a class="nav-about" href="#">ABOUT US</a>
    <a class="nav-services" href="#">SERVICES</a>
    <a class="nav-financing" href="#">FINANCING OPTIONS</a>
    <a class="nav-contact" href="#">CONTACT US</a>
    <div class="nav-search">Search...
      <span class="nav-search-btn">
        <svg width="10" height="10" viewBox="0 0 10 10"><circle cx="4" cy="4" r="3" stroke="#fff" stroke-width="1.4" fill="none"/><path d="M6 6l3.5 3.5" stroke="#fff" stroke-width="1.6"/></svg>
      </span>
    </div>
  </nav>
</header>

<h1 class="page-title">Financing Options</h1>
<div class="title-rule"></div>

<main class="article">
  <p>Mauris fermentum dictum magna. Sed laoreet aliquam lellus dolor, dapibus eget, elementum vel, cursus eleifend, elit.<br>Fusce temph or sodales massa ac cursus. Donec congue eleifejf rpnd est eu placerat. Suspendisse gravida turpis at metus placerat mattis. Phasellus tincidunt nisl at felis commodo lacinia nec vel quam. Proin auctor enim ipsum. Duis faucibus, ipsum ut ornare viverra, orci dolor mattis massa, ut scelerisque augue mauris vel diam.</p>
  <p>Donec at augue porttitor risus condimentum laoreet sed et leo. Donec consequat ipsum quis metus venenatis sagittis. Pellentesque fringilla sem vitae lorem pulvinar vel varius elit facilisis.</p>
  <p>Maecenas elementum urna ut velit ultrices quis bibendum odio suscipit. Vestibulum sit amet risus vel ligula viverra gravida vitae a arcu. Vivamus non ligula mi, vel sodales lacus. Nulla ac vehicula turpis.</p>
  <p>Donec sapien magna, suscipit et dignissim eget, scelerisque id sapien. Donec est tellus, elementum non auctor eu, iaculis vel nulla. Nam scelerisque pretium eleifend. Nulla aliquam est at magna fermentum mattis. Nullam imperdiet nulla at odio vehicula sagittisorem ipsum dolor sit amet, consectetuer adipiscing elit. Praesent vestibulum molestie lacus. Aenean nonummy hendrerit mauris. Phasellus porta. Fusce suscipit varius mi. Lorem ipsum dolor sit amet, consectetuer adipiscing elit. Praesent vestibulum molestie lacus. Morbi nunc odio, gravida at, cursus nec, luctus a, lorem. Maecenas tristique orci ac sem. Duis ultricies pharetra magna. Donec accumsan malesuadamonsectetuer adipiscing elit. Mauris fermentum dictum magna.</p>
</main>

<aside>
  <ul class="side-links">
    <li>Donec porta diam eu massa</li>
    <li>Quisque diam lorem</li>
    <li>Interdum vitae,dapibus ac</li>
    <li>Scelerisque vitae, pede</li>
    <li>Donec eget tellus non erat</li>
    <li>Lacinia fermentum</li>
    <li class="gap" style="padding:0"></li>
    <li>Tincidunt ac, viverra sed, nulla</li>
    <li>Donec porta diam eu massa</li>
    <li>Quisque diam loremInterdum</li>
    <li>vitae,dapibus acScelerisque vitae, pede</li>
    <li>Donec eget tellus non erat</li>
  </ul>
  <div class="side-photo photo-couple" role="img" aria-label="Couple embracing in front of their home"></div>
  <div class="side-photo photo-contract" role="img" aria-label="Model house beside a hand signing a contract"></div>
  <div class="side-photo photo-family" role="img" aria-label="Family playing on the lawn in front of a house"></div>
</aside>

<div class="section-rule"></div>

<section class="testimonial">
  <div class="testimonial-photo" role="img" aria-label="Handshake over a for sale sign marked sold"></div>
  <h2 class="testimonial-title">Testimonial</h2>
  <span class="quote-mark quote-open">“</span>
  <p class="testimonial-text">Nulla venenatis. In pede mi, aliquet sit amet, euismod in, auctor ut, ligula. Aliquam dapibus tincidunt metus. Praesent justo dolor.</p>
  <span class="quote-mark quote-close">”</span>
  <p class="testimonial-author">--Daniel Whitford Home Owner, NH</p>
</section>

<footer class="site-footer">
  <div class="footer-col col-about">
    <h3>About Us</h3>
    <ul><li>Company Info</li><li>Our Services</li><li>Clients</li><li>Partners</li></ul>
  </div>
  <div class="footer-col col-advice">
    <h3>Advice</h3>
    <ul><li>Sign up</li><li>Forums</li><li>Promotion</li><li>Career</li></ul>
  </div>
  <div class="footer-col col-join">
    <h3>Join In</h3>
    <ul><li>FAQs</li><li>Solutions</li><li>Sitemap</li><li>Contacts</li></ul>
  </div>
  <div class="newsletter">
    <h3>Join our Newsletter</h3>
    <div class="newsletter-input">Email Address:</div>
    <div class="newsletter-btn">Subscribe</div>
  </div>
  <div class="social"><span></span><span></span><span></span></div>
  <div class="footer-rule"></div>
  <p class="legal">Disclaimer &amp; Terms &amp; Conditions &nbsp;|&nbsp; Privacy Policy &nbsp;| Advertise With Us &nbsp;| &nbsp;Contact Us</p>
  <p class="copyright">Harbor Mortgage Relief &nbsp;© 2012. &nbsp;All Rights Reserved</p>
</footer>

</body>
</html>
```